Dorsey K. Whitfield Business Card

We need a business card for our company Dorsey K. Whitfield Heating & Plumbing to be distributed to potential customers. It should follow the color scheme of our logo and have a modern upscale and masculine look.

The logo is attached and the info below should also be included:

5187 W. Quarry Bend Rd.
Manheim, PA 17545

Tobias R. Whitfield
(717) 593-8126
tobiasreedwhitfield@mailvane.com
dorseykwhitfield.com
PA #038419

Industry/Entity Type

Business

Contact Information for Business Card

5187 W. Quarry Bend Rd.
Manheim, PA 17545

Tobias R. Whitfield
(717) 593-8126
tobiasreedwhitfield@mailvane.com
dorseykwhitfield.com
PA #038419

Colors

Designer to choose colors to be used in the design.

Requirements
Must have
• Information above included

```html
<!DOCTYPE html>
<html lang="en">
<head>
<meta charset="utf-8">
<title>Dorsey K. Whitfield Heating &amp; Plumbing — Business Card</title>
<link rel="stylesheet" href="https://fonts.googleapis.com/css2?family=Open+Sans:wght@400;600&family=Roboto:wght@700&display=swap">
<style>
  :root {
    --brand-blue: #1a6fae;
    --brand-blue-deep: #145f98;
    --brand-green: #7ab929;
    --card-bg: #f4f6f8;
    --page-bg: #d9d6d1;
    --ink: #222a31;
    --contact-ink: #eef3f8;
    --address-ink: #e3d6bb;
  }
  * { box-sizing: border-box; margin: 0; padding: 0; }
  html, body {
    width: 1200px; height: 1054px; overflow: hidden;
    background: var(--page-bg);
  }
  .card {
    position: absolute;
    left: 100px; top: 225px;
    width: 1000px; height: 603px;
    background: var(--card-bg);
    overflow: hidden;
    box-shadow: 0 10px 30px rgba(0,0,0,0.18);
    font-family: "Open Sans", Arial, sans-serif;
  }
  .card-wave { position: absolute; inset: 0; width: 100%; height: 100%; }

  .company {
    position: absolute; left: 57px; top: 60px;
    display: flex; align-items: center; gap: 18px;
  }
  .company-square {
    width: 118px; height: 118px; background: var(--brand-blue); flex: none;
  }
  .company-name {
    font-family: "Roboto", Arial, sans-serif;
    font-weight: 700; font-size: 40px; line-height: 1.1;
    color: var(--brand-blue); text-transform: uppercase;
    width: 470px;
  }

  .person { position: absolute; left: 57px; top: 268px; }
  .person-name {
    font-family: "Roboto", Arial, sans-serif;
    font-weight: 700; font-size: 38px; color: var(--brand-blue);
    letter-spacing: 0.2px;
  }
  .person-title { font-size: 23px; color: var(--ink); margin-top: 6px; }
  .person-license { font-size: 23px; color: var(--ink); margin-top: 22px; }
  .person-license .state { color: var(--brand-blue); }

  .contact {
    position: absolute; right: 50px; top: 413px;
    list-style: none; text-align: right;
  }
  .contact-item {
    display: flex; justify-content: flex-end; align-items: center; gap: 16px;
    font-size: 23px; line-height: 47px; color: var(--contact-ink);
  }
  .contact-item svg { width: 22px; height: 22px; flex: none; }
  .contact-address { color: var(--address-ink); padding-right: 0; }
</style>
</head>
<body>
  <article class="card">
    <svg class="card-wave" viewBox="0 0 1000 603" preserveAspectRatio="none" aria-hidden="true">
      <path fill="var(--brand-blue)" d="M0 505 C 240 565, 450 545, 630 425 C 770 330, 890 302, 1000 298 L1000 603 L0 603 Z"/>
      <path fill="var(--brand-green)" d="M0 440 C 210 525, 430 530, 625 400 C 765 305, 885 268, 1000 260 L1000 282 C 885 292, 770 325, 630 420 C 430 560, 210 545, 0 478 Z"/>
    </svg>

    <header class="company">
      <div class="company-square"></div>
      <div class="company-name">Dorsey K. Whitfield Heating &amp; Plumbing</div>
    </header>

    <section class="person">
      <h1 class="person-name">Tobias R. Whitfield</h1>
      <p class="person-title">Managing Director</p>
      <p class="person-license"><span class="state">PA</span> #038419</p>
    </section>

    <ul class="contact">
      <li class="contact-item">(717) 593-8126
        <svg viewBox="0 0 24 24" aria-hidden="true"><path fill="#fff" d="M3 9c0-3 4-5 9-5s9 2 9 5v1h-5V8H8v2H3zm4 2h10l3 9H4zm5 2a3 3 0 1 0 0 6 3 3 0 0 0 0-6z"/></svg>
      </li>
      <li class="contact-item">dorseykwhitfield.com
        <svg viewBox="0 0 24 24" aria-hidden="true"><rect x="2" y="5" width="20" height="14" fill="#fff"/><path d="M2 5l10 8 10-8" fill="none" stroke="var(--brand-blue)" stroke-width="2"/></svg>
      </li>
      <li class="contact-item">tobiasreedwhitfield@mailvane.com
        <svg viewBox="0 0 24 24" aria-hidden="true"><g fill="none" stroke="#fff" stroke-width="2"><circle cx="12" cy="12" r="9"/><ellipse cx="12" cy="12" rx="4" ry="9"/><path d="M3 12h18M5 7h14M5 17h14"/></g></svg>
      </li>
      <li class="contact-item contact-address">5187 W. Quarry Bend Rd. Manheim, PA 17545</li>
    </ul>
  </article>
</body>
</html>
```